postcard design for a design company to promote itself in a new area

I am putting out postcards to hairdressing salons that I have renovated recently to target there client base and to offer a discount to the initial consult to there loyal clients. I would like to have a vibrant front design that I can change every twelve weeks with my logo (existing) imbedding into a vibrate, energetic, stylish yet creative front. I want something very colourful fun and inviting that makes people want to pick it up, it should contain some style of pattern and I don't want it all to be my logo. My existing logo I would like on the front but only small or built into the pattern it can be in a different colour and the out side shape can change as long its still the same letters etc.. The pattern can contain words.. The following is what I have written that will be on the back of the post card so you can understand the feel of it.

Lorelle from Kestrel Interiors is partnering up with Marisol and Wendy from Bobbin Cuts
As we have something special in common, we both want our clients to look & feel fabulous
Lorelle is offering the loyal clients of Bobbin Cuts a special in home consult at a reduced rate.
What we do: Create innovative yet practical design solutions, window treatments & furniture, which are stylish, happy & memorable. Design to us is about you, who you are & how you live, we are passionate about creating a space that is for you and about you.
A well-designed space makes you feel 10 years younger and truly fabulous to be in, it does not have to cost the earth, but it is something everyone should go home to…
Call today to find out how we can add value & create a space that makes you feel wonderful to be in.
m 0413 972 016

Any suggestions on the wording would be appreciated... Especially the 'A well designed space makes you feel 10years younger'

I have attached my existing logo the colour can change.

I want to reach out to the people sitting in the chair getting there hair done and make them want to know a little more about my business. I would like the post card to feel fresh young new and happy.

```html
<!DOCTYPE html>
<html lang="en">
<head>
<meta charset="utf-8">
<title>Kestrel Interiors – Postcard</title>
<link rel="stylesheet" href="https://fonts.googleapis.com/css2?family=Questrial&family=Kalam:wght@400;700&display=swap">
<style>
  :root{
    --charcoal:#2c2e30;
    --magenta:#e32bc4;
    --cyan:#1fd6ec;
    --lime:#8fe01d;
    --white:#ffffff;
    --ink:#1d1d1d;
    --photo-shadow:rgba(0,0,0,.55);
  }
  html,body{margin:0;padding:0;width:1200px;height:1150px;overflow:hidden;background:var(--white);}
  .stage{position:absolute;left:0;top:0;width:945px;height:900px;transform:scale(1.2698);transform-origin:0 0;}
  .card{position:absolute;left:55px;width:835px;height:395px;background:var(--charcoal);overflow:hidden;}
  .card--front{top:50px;}
  .card--back{top:458px;}
  .card__waves{position:absolute;inset:0;width:100%;height:100%;}
  .photo{position:absolute;box-shadow:6px 8px 12px var(--photo-shadow);}
  .photo--table{left:0;top:50px;width:180px;height:230px;background:linear-gradient(135deg,#b7d43a,#e9e4d0 55%,#8a7a5a);}
  .photo--bed{left:195px;top:100px;width:218px;height:146px;background:linear-gradient(160deg,#dfe7ea,#f1b58f 55%,#e9a47c);}
  .photo--dresser{left:430px;top:60px;width:175px;height:212px;background:linear-gradient(180deg,#f2f2ee,#3a7fa8 35%,#5a1a1e 65%,#4a1418);}
  .photo--shelf{left:640px;top:60px;width:195px;height:138px;background:linear-gradient(120deg,#2f4a3c,#6a8a4a 50%,#d9c9b0);}
  .tagline{position:absolute;left:40px;top:310px;width:460px;margin:0;text-align:center;color:var(--white);
    font-family:"Kalam",cursive;font-weight:700;font-size:22px;line-height:27px;}
  .brand{position:absolute;width:139px;height:147px;background:var(--lime);box-shadow:5px 6px 10px var(--photo-shadow);
    display:flex;align-items:flex-end;justify-content:center;}
  .brand__name{font-family:"Questrial",sans-serif;color:var(--white);font-size:11px;letter-spacing:1.2px;margin-bottom:10px;text-transform:uppercase;}
  .card--front .brand{left:671px;top:230px;}
  .card--back .brand{left:668px;top:224px;}
  .panel{position:absolute;left:52px;top:47px;width:726px;height:295px;background:var(--white);box-shadow:4px 6px 12px var(--photo-shadow);}
  .photo--round{position:absolute;left:33px;top:10px;width:124px;height:124px;border-radius:50%;
    background:radial-gradient(circle at 40% 40%,#4e8a3c,#f4f4f0 60%,#e4e2dc);box-shadow:3px 5px 10px var(--photo-shadow);}
  .copy{font-family:"Questrial",sans-serif;color:var(--ink);margin:0;}
  .copy--intro{position:absolute;left:165px;top:22px;width:530px;text-align:center;font-size:13.4px;line-height:17px;}
  .heading{position:absolute;left:160px;top:100px;width:540px;text-align:center;margin:0;
    font-family:"Questrial",sans-serif;font-weight:700;font-size:17px;color:var(--cyan);letter-spacing:.3px;}
  .copy--services{position:absolute;left:150px;top:122px;width:560px;text-align:center;font-size:12.6px;line-height:16.5px;}
  .copy--promise{position:absolute;left:40px;top:184px;width:560px;font-size:12.6px;line-height:17px;}
  .copy--call{position:absolute;left:40px;top:228px;font-family:"Kalam",cursive;font-size:11px;}
  .phone{position:absolute;left:40px;top:252px;margin:0;font-family:"Questrial",sans-serif;font-weight:700;font-size:17px;color:var(--cyan);letter-spacing:.5px;}
</style>
</head>
<body>
<main class="stage">

  <section class="card card--front" aria-label="Postcard front">
    <svg class="card__waves" viewBox="0 0 835 395" preserveAspectRatio="none" aria-hidden="true">
      <path d="M0 62 C250 25 600 60 835 150 V262 C650 205 420 150 0 118 Z" fill="var(--cyan)"/>
      <path d="M0 0 H835 V62 C620 8 300 -4 0 42 Z" fill="var(--magenta)"/>
      <path d="M0 42 C300 -4 620 8 835 62 V78 C620 28 300 16 0 56 Z" fill="#111"/>
      <path d="M360 252 C540 240 720 252 835 286 V298 C720 264 540 254 360 264 Z" fill="var(--lime)"/>
      <path d="M180 262 C400 250 650 262 835 312 V328 C650 280 400 268 180 278 Z" fill="var(--white)"/>
    </svg>
    <div class="photo photo--table" role="img" aria-label="Photo: dining table set with lilies against a lime wall"></div>
    <div class="photo photo--bed" role="img" aria-label="Photo: bed with peach patterned cover beside a bright window"></div>
    <div class="photo photo--dresser" role="img" aria-label="Photo: timber dresser with potted plant, blue artwork and necklaces"></div>
    <div class="photo photo--shelf" role="img" aria-label="Photo: glass vases with plants in front of a green wall with prints"></div>
    <p class="tagline">We can add value &amp; create a space<br>that makes you feel wonderful to be in.</p>
    <div class="brand"><span class="brand__name">Kestrel Interiors</span></div>
  </section>

  <section class="card card--back" aria-label="Postcard back">
    <svg class="card__waves" viewBox="0 0 835 395" preserveAspectRatio="none" aria-hidden="true">
      <path d="M0 14 C80 2 150 2 230 12 V22 C150 12 80 12 0 26 Z" fill="var(--lime)"/>
      <path d="M0 28 C80 14 150 14 230 24 V34 C150 26 80 26 0 40 Z" fill="var(--cyan)"/>
      <path d="M140 0 H835 V40 C650 6 400 -2 140 0 Z" fill="var(--magenta)"/>
      <path d="M560 20 C680 28 770 40 835 58 V72 C770 52 680 40 560 32 Z" fill="var(--cyan)"/>
      <path d="M760 236 C790 240 815 246 835 254 V266 C815 258 790 252 760 248 Z" fill="var(--lime)"/>
    </svg>
    <div class="panel">
      <div class="photo--round" role="img" aria-label="Photo: white sideboard styled with tall leafy plants"></div>
      <p class="copy copy--intro">Lorelle from Kestrel Interiors is partnering up with Marisol and Wendy from Bobbin Cuts As we have something special in common, we both want our clients to look &amp; feel fabulous Lorelle is offering the loyal clients of Bobbin Cuts a special in home consult at a reduced rate.</p>
      <h2 class="heading">WHAT WE DO</h2>
      <p class="copy copy--services">Create innovative yet practical design solutions, window treatments &amp; furniture, which are stylish, happy &amp; memorable. Design to us is about you, who you are &amp; how you live, we are passionate about creating a space that is for you and about you.</p>
      <p class="copy copy--promise">A well-designed space makes you feel 10 years younger and truly fabulous to be in,<br>it does not have to cost the earth, but it is something everyone should go home to…</p>
      <p class="copy copy--call">Call today to find out how we can add value &amp; create a space that makes you feel wonderful to be in.</p>
      <p class="phone">M 0413 972 016</p>
    </div>
    <div class="brand"><span class="brand__name">Kestrel Interiors</span></div>
  </section>

</main>
</body>
</html>
```